Steady Harbor Claims Group Business card

Need a business card that stands out that includes name of company,(above) Owners name Moira Lindqvist phone#517-362-4408 email# SteadyHarborCG@mailvane.com and website www.Steadyharborclaimsgroup.net. This is a medical billing company so the card has to relate to that or relate to increasing revenue

```html
<!DOCTYPE html>
<html lang="en">
<head>
<meta charset="utf-8">
<title>Steady Harbor Claims Group — Business Card</title>
<link rel="stylesheet" href="https://fonts.googleapis.com/css2?family=Marcellus+SC&family=Open+Sans:wght@400&display=swap">
<style>
  :root {
    --navy: #0d3a80;
    --navy-deep: #0a347a;
    --growth-green: #6aae2a;
    --paper: #e9eaec;
    --ink: #2e3136;
    --white: #ffffff;
    --backdrop: #d9dadc;
  }
  * { margin: 0; padding: 0; box-sizing: border-box; }
  html, body {
    width: 1105px; height: 1200px; overflow: hidden;
    background: var(--backdrop);
  }
  .sheet { position: relative; width: 1105px; height: 1200px; }
  .card {
    position: absolute; left: 179px; width: 747px; height: 427px; overflow: hidden;
  }
  .card--front { top: 119px; background: var(--paper); }
  .card--back { top: 637px; background: var(--navy-deep); }

  .front-field { position: absolute; inset: 0; }

  .owner {
    position: absolute; left: 40px; top: 34px; color: var(--white);
    font-family: "Marcellus SC", serif;
  }
  .owner__name { font-size: 33px; letter-spacing: 0.5px; line-height: 1.1; }
  .owner__title { font-size: 21px; letter-spacing: 0.5px; opacity: 0.92; }

  .brand {
    position: absolute; left: 420px; top: 150px; width: 300px;
    display: flex; flex-direction: column; align-items: center; gap: 14px;
  }
  .brand__mark { width: 52px; height: 52px; border-radius: 50%; background: var(--growth-green); }
  .brand__name {
    font-family: "Marcellus SC", serif; font-size: 24px; color: var(--navy);
    letter-spacing: 0.5px; text-align: center; line-height: 1.15;
  }

  .contacts {
    position: absolute; right: 34px; top: 308px; list-style: none;
    font-family: "Open Sans", sans-serif; font-size: 18.5px; color: var(--ink);
  }
  .contacts__item {
    display: flex; justify-content: flex-end; align-items: center; gap: 14px;
    height: 28.5px;
  }
  .contacts__icon { width: 18px; height: 18px; flex: none; }

  .back-brand {
    position: absolute; left: 0; right: 0; top: 270px; text-align: center; color: var(--white);
  }
  .back-brand__name {
    font-family: "Marcellus SC", serif; font-size: 30px; letter-spacing: 1px; line-height: 1.15;
  }
  .back-brand__web {
    font-family: "Open Sans", sans-serif; font-size: 19px; margin-top: 6px;
  }
</style>
</head>
<body>
<main class="sheet">
  <section class="card card--front" aria-label="Business card front">
    <svg class="front-field" width="747" height="427" viewBox="0 0 747 427" role="img" aria-label="Navy field where the rising growth-arrow graphic belongs">
      <polygon points="0,0 530,0 0,346" fill="var(--navy)"/>
    </svg>

    <div class="owner">
      <p class="owner__name">Moira Lindqvist</p>
      <p class="owner__title">Owners</p>
    </div>

    <div class="brand">
      <span class="brand__mark" aria-hidden="true"></span>
      <p class="brand__name">Steady Harbor<br>Claims Group</p>
    </div>

    <ul class="contacts">
      <li class="contacts__item">517-362-4408
        <svg class="contacts__icon" viewBox="0 0 24 24" aria-hidden="true"><path fill="var(--navy)" d="M6.6 10.8a15 15 0 0 0 6.6 6.6l2.2-2.2c.3-.3.7-.4 1-.2 1.1.4 2.3.6 3.6.6.6 0 1 .4 1 1V20c0 .6-.4 1-1 1A17 17 0 0 1 3 4c0-.6.4-1 1-1h3.5c.6 0 1 .4 1 1 0 1.300.2 2.500.6 3.600.1.3 0 .7-.2 1z"/></svg>
      </li>
      <li class="contacts__item">SteadyHarborCG@mailvane.com
        <svg class="contacts__icon" viewBox="0 0 24 24" aria-hidden="true"><rect x="2" y="5" width="20" height="14" rx="1.5" fill="var(--navy)"/><path d="M3 6.5l9 6.5 9-6.5" fill="none" stroke="var(--paper)" stroke-width="1.6"/></svg>
      </li>
      <li class="contacts__item">Steadyharborclaimsgroup.net
        <svg class="contacts__icon" viewBox="0 0 24 24" aria-hidden="true"><circle cx="12" cy="12" r="10" fill="var(--navy)"/><path d="M12 2v20M2 12h20M5 6.5c4 2 10 2 14 0M5 17.5c4-2 10-2 14 0" fill="none" stroke="var(--paper)" stroke-width="1.3"/></svg>
      </li>
    </ul>
  </section>

  <section class="card card--back" aria-label="Business card back">
    <div class="back-brand">
      <p class="back-brand__name">Steady Harbor<br>Claims Group</p>
      <p class="back-brand__web">Steadyharborclaimsgroup.net</p>
    </div>
  </section>
</main>
</body>
</html>
```